Tour Guide in Israel business card

I am a tour guide in Israel (the holy land). Prior to it I have over 20 years high-tech business. My main (but not only) focus is working with business people that come to Israel and want to get a tour (usually short from few hours to 2 days). During my guiding I incorporate a lot of my know how of the Israeli business culture. I like to have a business card that I can present to anyone that is looking for a tour guide, but that business people will understand the additional value I can provide them during my tour.

Target Market(s)

Business visitors and tourist to Israel

Industry/Entity Type

Tourism

Contact Information for Business Card

Dorian Kaplow
email: dorian@kaplowtours.net
Mobile: +972-52-7186450

Colors

Designer to choose colors to be used in the design.

Requirements
Must have
• Tour Guide
Nice to have
• I don't know how but it should project my understanding in business not just the tourist side of my knowledge.

```html
<!DOCTYPE html>
<html lang="en">
<head>
<meta charset="utf-8">
<title>Dorian Kaplow – Tour Guide Business Card</title>
<link href="https://fonts.googleapis.com/css2?family=Roboto:wght@300;400;900&display=swap" rel="stylesheet">
<style>
  :root {
    --backdrop: #1e1e1f;
    --card-white: #f2f2f2;
    --card-white-shade: #d9d9d9;
    --ink-navy: #0f2a44;
    --ink-grey: #4a4a4a;
    --card-blue-top: #1f6b96;
    --card-blue-bottom: #05192b;
    --glow-cyan: #3fc6ff;
    --web-text: #e6eef4;
  }
  * { box-sizing: border-box; margin: 0; padding: 0; }
  html, body {
    width: 1200px;
    height: 890px;
    overflow: hidden;
    background: var(--backdrop);
    font-family: "Roboto", Arial, sans-serif;
  }
  .canvas {
    position: relative;
    width: 1200px;
    height: 890px;
  }
  .card {
    position: absolute;
    top: 165px;
    width: 340px;
    height: 560px;
    box-shadow: 0 18px 40px rgba(0,0,0,0.55);
    overflow: hidden;
  }
  .card-front {
    left: 230px;
    background: linear-gradient(160deg, var(--card-white) 0%, var(--card-white-shade) 100%);
  }
  .contact-block {
    position: absolute;
    left: 40px;
    right: 30px;
    bottom: 100px;
    color: var(--ink-navy);
  }
  .name-first {
    font-size: 38px;
    font-weight: 300;
    line-height: 1;
    letter-spacing: 0.5px;
  }
  .name-last {
    font-size: 38px;
    font-weight: 900;
    line-height: 1.05;
  }
  .job-title {
    font-size: 13px;
    font-weight: 400;
    letter-spacing: 3px;
    color: var(--ink-navy);
    margin: 6px 0 16px;
  }
  .contact-line {
    font-size: 18px;
    font-weight: 400;
    color: var(--ink-grey);
    line-height: 1.4;
  }
  .card-back {
    left: 630px;
    background: radial-gradient(circle at 65% 30%, var(--card-blue-top) 0%, var(--card-blue-bottom) 95%);
  }
  .map-network {
    position: absolute;
    left: 105px;
    top: 80px;
    width: 150px;
    height: 330px;
    border-radius: 50% 50% 45% 45% / 30% 30% 70% 70%;
    background: radial-gradient(ellipse at 50% 45%, rgba(63,198,255,0.5) 0%, rgba(63,198,255,0.15) 60%, rgba(63,198,255,0) 100%);
  }
  .website {
    position: absolute;
    left: 30px;
    right: 30px;
    bottom: 80px;
    text-align: center;
    color: var(--web-text);
    font-size: 15px;
    font-weight: 400;
    letter-spacing: 4px;
    white-space: nowrap;
  }
</style>
</head>
<body>
  <main class="canvas">
    <section class="card card-front">
      <div class="contact-block">
        <p class="name-first">DORIAN</p>
        <p class="name-last">KAPLOW</p>
        <p class="job-title">TOUR GUIDE</p>
        <p class="contact-line">+972-52-7186450</p>
        <p class="contact-line">dorian@kaplowtours.net</p>
      </div>
    </section>
    <section class="card card-back">
      <div class="map-network" role="img" aria-label="Glowing connected-dot network drawing of the map of Israel"></div>
      <p class="website">WWW.KAPLOWTOURS.NET</p>
    </section>
  </main>
</body>
</html>
```